PREMIUM Pagewall Page Design - A+++ Designers Wanted

** DO NOT ATTEMPT TO CONTACT ME THROUGH SEARCHING ON SEEKRA OR EMAILING ME THROUGH MY WEBSITE **

I need an amazing, fresh, contemporary Pagewall banner design created, using supplied photos.

You must be able to excellent graphics deisgn and photoshop skills to 'manipulate' photos to extend them / modify them for working on a horizontal banner.

Target Market(s)

Agency, Advertising Agency, Creative, Designers, Social Media, Online

Industry/Entity Type

Seekra

Font styles to use
Serif
Sans Serif

Requirements
Must have
• It must be fresh, clean, uncluttered and bold, and have text in the same font style (Arial Bold).
• Here are the photos you can download to choose from https://www.filecrate-share.example/sh/47kkwpt219qmzav/BCDnYPT1z6L5Fhyk8j1FcNcJb?dl=0
• For Text Style Sample : You can use any combination of Yellow, Black, White and Blue as per "SAMPLE UPLOAD FILE 1".
• Text : Pagewall Text must say "MAKING CENTURY OLD STORY TELLING A BRAND NEW EXPERIENCE" (see www.pagewall.example/fastlakeow for example)
• Second Project - To be awarded to winner of Pagewall project and paid additional $$
• Blurtix Text: I am open to designs and styles here. You can try any combination of "OWEN FASTLAKE" logo (see attached) and words like "GLOBAL FUTURIST" "STORY TELLER". I will leave you to design some ideas.
• The image must also be viewable on mobile & desktop, without losing any text.
• The 'profile' headshot photo for both can also be changed to suit your design.
Nice to have
• Must have a premium, fresh and uncluttered look. You should explore how to get the most out of the photos, and can edit them to create / extend the image to make it fit the banner space.
Should not have
• No funny or silly standard / off the shelf designs
• ** DO NOT ATTEMPT TO CONTACT ME THROUGH SEARCHING ON SEEKRA OR EMAILING ME THROUGH MY WEBSITE **

```html
<!DOCTYPE html>
<html lang="en">
<head>
<meta charset="utf-8">
<title>Making Century Old Story Telling – Pagewall Banner</title>
<link href="https://fonts.googleapis.com/css2?family=Open+Sans:wght@700&display=swap" rel="stylesheet">
<style>
  :root {
    --ink: #050505;
    --headline-yellow: #f4ef1e;
    --headline-white: #ffffff;
    --scene-green: #1f6b4a;
    --scene-teal: #1b5d8a;
    --scene-blue: #3a3fc4;
    --scene-violet: #6a4fe0;
    --scene-deep: #15173f;
    --chevron-light: #d9e6f2;
    --portrait-light: #d9c2bd;
    --portrait-mid: #9a7f86;
    --portrait-shadow: #5b4a6e;
  }

  * { margin: 0; padding: 0; box-sizing: border-box; }

  html, body {
    width: 1200px;
    height: 445px;
    overflow: hidden;
    background: var(--ink);
  }

  .banner {
    position: relative;
    width: 1200px;
    height: 445px;
    overflow: hidden;
    font-family: "Open Sans", Arial, sans-serif;
    font-weight: 700;
  }

  .banner__scene {
    position: absolute;
    inset: 0;
    background:
      radial-gradient(ellipse 420px 300px at 120px 150px, rgba(60,150,70,0.55), transparent 70%),
      linear-gradient(100deg, var(--scene-green) 0%, var(--scene-teal) 30%, var(--scene-blue) 60%, var(--scene-violet) 85%, var(--scene-deep) 100%);
  }

  .banner__skyline {
    position: absolute;
    left: 0;
    bottom: 0;
    width: 760px;
    height: 130px;
    background: linear-gradient(180deg, rgba(40,60,170,0.0) 0%, rgba(35,45,150,0.55) 45%, rgba(30,40,140,0.75) 100%);
  }

  .banner__chevron {
    position: absolute;
    top: 0;
    left: 0;
    width: 1200px;
    height: 445px;
  }

  .banner__portrait {
    position: absolute;
    top: 0;
    right: 0;
    width: 300px;
    height: 445px;
    background: linear-gradient(100deg, var(--portrait-shadow) 0%, var(--portrait-mid) 30%, var(--portrait-light) 65%, var(--portrait-mid) 100%);
  }

  .headline {
    position: absolute;
    left: 0;
    top: 0;
    width: 1200px;
    height: 445px;
  }

  .headline__block {
    position: absolute;
    background: var(--ink);
    text-transform: uppercase;
    text-align: right;
    line-height: 1.12;
    font-size: 48px;
    letter-spacing: 0.2px;
  }

  .headline__block--lead {
    left: 290px;
    top: 54px;
    width: 562px;
    height: 140px;
    padding: 11px 22px 0 0;
    color: var(--headline-yellow);
  }

  .headline__block--tail {
    left: 290px;
    top: 218px;
    width: 562px;
    height: 138px;
    padding: 14px 22px 0 0;
    color: var(--headline-white);
    clip-path: polygon(0 0, 100% 0, 100% 100%, 22.4% 100%, 22.4% 34.8%);
  }

  .headline__line { display: block; white-space: nowrap; }
</style>
</head>
<body>
  <main class="banner">
    <div class="banner__scene" role="img" aria-label="Futuristic green-to-violet cityscape backdrop with hexagon grid and flying drone"></div>
    <div class="banner__skyline" role="img" aria-label="City skyline silhouette along the bottom edge"></div>

    <svg class="banner__chevron" viewBox="0 0 1200 445" aria-hidden="true">
      <polygon points="790,0 880,0 1060,220 880,445 790,445 970,220" fill="var(--chevron-light)" opacity="0.85"/>
    </svg>

    <div class="banner__portrait" role="img" aria-label="Close-up portrait of the storyteller, right half of face"></div>

    <h1 class="headline">
      <span class="headline__block headline__block--lead">
        <span class="headline__line">Making Century</span>
        <span class="headline__line">Old Story Telling</span>
      </span>
      <span class="headline__block headline__block--tail">
        <span class="headline__line">A Brand New</span>
        <span class="headline__line">Experience</span>
      </span>
    </h1>
  </main>
</body>
</html>
```